This book will apply the 12 Steps to gaming addiction, also known as video game addiction. The primary purpose of the book is to provide an effective solution for this new type of addiction. The solution is based on the rich and successful concepts of traditional twelve-step programs like RL.

The title on the cover will be "Nine Doors Past the Glowing Screen" and "by Martin Quorby". A subtitle can be used if it works in your design of "A Practical Path Beyond Compulsive Console Play". Cover will be for a 6" x 9" book approximately 110 pages in length.

Some back cover text including some review quotes and an author bio are in the attached Word doc. There is also an author photo attached for for the back cover.

Requirements
Must have
• For the cover design it could be stylized, or an image, a partial image, or whatever. I am open to suggestions. Think about what would be noticed by a person searching for help with moderating their video game use, or by the parents or loved ones of problem gamers. Something contemporary and eye catching.

```html
<!DOCTYPE html>
<html lang="en">
<head>
<meta charset="utf-8">
<title>Nine Doors Past the Glowing Screen — Book Cover</title>
<link rel="stylesheet" href="https://fonts.googleapis.com/css2?family=Oswald:wght@500;600&family=Montserrat:wght@700&family=Source+Serif+4:opsz,wght@8..60,400&display=swap">
<style>
  :root {
    --page-bg: #d9d4cc;
    --back-bg: #100e20;
    --front-bg: #130f36;
    --front-deep: #0f0b2e;
    --accent-blue: #1ba6ea;
    --accent-orange: #f07b22;
    --text-light: #ffffff;
    --rule-orange: #e0631c;
  }
  * { margin: 0; padding: 0; box-sizing: border-box; }
  html, body { width: 1200px; height: 936px; overflow: hidden; background: var(--page-bg); }

  .book-spread {
    position: absolute; left: 76px; top: 61px;
    width: 1049px; height: 725px;
    display: flex;
    box-shadow: 3px 5px 10px rgba(0,0,0,0.35);
  }

  /* Back cover */
  .back-cover {
    position: relative; width: 484px; height: 100%;
    background: var(--back-bg);
    font-family: "Source Serif 4", Georgia, serif;
    font-size: 9.6px; line-height: 12px; color: var(--text-light);
  }
  .back-column {
    position: absolute; left: 61px; top: 64px; width: 366px;
  }
  .praise, .blurb { text-align: justify; hyphens: auto; }
  .praise { color: var(--accent-blue); }
  .praise p, .blurb p { margin-bottom: 12px; }
  .praise .tight { margin-bottom: 0; }
  .praise-rule {
    border-top: 1px solid var(--rule-orange);
    margin: 0 0 12px;
  }
  .about {
    display: flex; gap: 24px; margin-top: 18px; margin-left: -4px;
  }
  .author-photo {
    flex: 0 0 105px; height: 104px; margin-top: 8px;
    background: radial-gradient(circle at 50% 45%, #8a6a55 0%, #4d5a3a 55%, #2b3424 100%);
  }
  .author-bio { flex: 1; text-align: justify; }
  .author-bio h3 { font-weight: 400; font-size: 9.6px; margin-bottom: 12px; }

  /* Spine */
  .spine {
    position: relative; width: 80px; height: 100%;
    background: var(--front-bg);
  }
  .spine-title, .spine-author {
    position: absolute; left: 50%; white-space: nowrap;
    transform: translate(-50%, -50%) rotate(-90deg);
    color: var(--text-light);
  }
  .spine-title {
    top: 291px;
    font-family: "Oswald", sans-serif; font-weight: 600; font-size: 25px;
  }
  .spine-title .highlight { color: var(--accent-orange); }
  .spine-author {
    top: 618px;
    font-family: "Montserrat", sans-serif; font-weight: 700; font-size: 18px;
  }

  /* Front cover */
  .front-cover {
    position: relative; width: 485px; height: 100%;
    background: var(--front-bg);
    text-align: center; overflow: hidden;
  }
  .front-author {
    position: absolute; top: 38px; width: 100%;
    font-family: "Montserrat", sans-serif; font-weight: 700; font-size: 19px;
    line-height: 22px; color: var(--text-light);
  }
  .front-title {
    position: absolute; top: 96px; left: 0; width: 100%;
    font-family: "Oswald", sans-serif; font-weight: 500;
  }
  .title-top { display: block; color: var(--accent-blue); font-size: 54px; line-height: 64px; }
  .title-link {
    display: flex; align-items: center; justify-content: center; gap: 8px;
    font-family: "Montserrat", sans-serif; font-weight: 700; font-size: 23px;
    color: var(--text-light); line-height: 28px;
  }
  .title-link::before, .title-link::after {
    content: ""; width: 133px; border-top: 2px solid var(--text-light);
  }
  .title-bottom { display: block; color: var(--accent-orange); font-size: 44px; line-height: 58px; }

  .cover-image {
    position: absolute; left: 0; top: 331px; width: 485px; height: 332px;
    background:
      radial-gradient(ellipse at 85% 40%, rgba(190,190,210,0.55) 0%, rgba(90,100,200,0.25) 35%, transparent 60%),
      radial-gradient(ellipse at 75% 88%, rgba(120,140,255,0.55) 0%, transparent 50%),
      radial-gradient(ellipse at 25% 60%, rgba(40,50,120,0.9) 0%, transparent 60%),
      linear-gradient(180deg, var(--front-bg) 0%, #26308f 55%, #1b1e70 100%);
  }
</style>
</head>
<body>
  <div class="book-spread">
    <section class="back-cover">
      <div class="back-column">
        <div class="praise">
          <p>Praise for Nine Doors Past the Glowing Screen</p>
          <p>“A must-read for anyone who is addicted to or thinks they may have a problem with digital gaming. This eloquent work will also be useful to academics and clinicians exploring potential solutions. The author recognizes the similarities between gaming addiction and other addictions, and logically applies one of the most effective known solutions for addiction - The Twelve Steps.”</p>
          <p>-- Dale Wrenfield, Noted Interventionist and Keynote Speaker</p>
          <p class="tight">“If you suffer from digital gaming addiction, I strongly encourage you to use this book as your road map to get you back to the real world.”</p>
          <p class="tight">-- Owen Prasky, Founder of Brightline Media Review.</p>
          <p>“As a high school teacher for 24 years, husband, father, coach, and 12-Step member, I can assure you that this book will transform the life of anyone who is addicted to video games. Well written, easy to understand, and a wonderful book that will provide you with a clear road map to recovery, and this includes teenagers, a group I have been working with in the classroom for decades.”</p>
          <p>-- Tobias Merrin, Harlow Bay, OR High School Teacher.</p>
        </div>
        <div class="praise-rule"></div>
        <div class="blurb">
          <p>A practical path beyond compulsive console play (aka Video Game Addiction) based on the rich and successful tradition of the Twelve Steps.</p>
          <p>Addiction to Digital Gaming is a new and troubling phenomenon that has burst upon an unprepared society with alarming speed. Many people crave the use of Digital Games in a strikingly similar way to any other addict. Digital Games are a complex software and hardware system that have been designed to promote continued and progressive usage. This sophisticated technology clearly feeds on natural addictive tendencies.</p>
          <p>The 12 Steps are one of the most effective methods for treating addiction in human history. Originating with Recovery League in 1939, the 12 Steps have since been used to treat a variety of other addictions, including drugs, sex, gambling, eating disorders, and many others. Now in this groundbreaking work the 12 Steps are applied to the complex and evolving contemporary phenomenon of Digital Gaming Addiction.</p>
        </div>
        <div class="about">
          <div class="author-photo" role="img" aria-label="Portrait photo of the author"></div>
          <div class="author-bio">
            <h3>About the Author</h3>
            <p>Martin Quorby is a Technology Consultant and Writer with many years of professional coding and consulting experience. He also struggled with addiction to drugs and alcohol and is now clean and sober in a Twelve-Step program for over 17 years. This unique combination of 12-Step experience and technology expertise led him to create Nine Doors Past the Glowing Screen.</p>
          </div>
        </div>
      </div>
    </section>

    <section class="spine">
      <div class="spine-title">Nine Doors Past the <span class="highlight">Glowing Screen</span></div>
      <div class="spine-author">Martin Quorby</div>
    </section>

    <section class="front-cover">
      <div class="front-author">Martin Quorby</div>
      <h1 class="front-title">
        <span class="title-top">Nine Doors</span>
        <span class="title-link">PAST THE</span>
        <span class="title-bottom">Glowing Screen</span>
      </h1>
      <div class="cover-image" role="img" aria-label="Photo of a young gamer wearing a headset, seen from the side, typing at a glowing keyboard in front of two monitors showing static"></div>
    </section>
  </div>
</body>
</html>
```